Sleek Design For Personal Brand Wordpress Website !!

*WORDPRESS WEBSITE*

Need a sleek and easy to navigate Wordpress website.

It will act as the hub for my personal brand.

Which means it will showcase all my social media outlets, host my most recent content like youtube videos and podcasts...

It will also be the go to place to find all my digital products and services that I offer.

i want it to be super sleek and simple but also give a personal touch of my who I really am. You can get a good idea of who I am my checking out my Instagram (@karel.dumonte)

Use these websites for ideas: www.brevanhollis.example and www.dorianfelkowitz.example

Target Market(s)

Young Entrepreneurs

Industry/Entity Type

Education

Logo Text

Karel Dumonte

Number of Pages Required

4 page

Font styles to use
Sans Serif

Colors
ffffff
0392cd
ec1f27

Requirements
Must have
• Social Media buttons on the home page...
• Video (also a slider) right at the top of the home page...
• Email Optin...
• Multiple pages...

```html
<!DOCTYPE html>
<html lang="en">
<head>
<meta charset="utf-8">
<title>Karel Dumonte</title>
<link rel="stylesheet" href="https://fonts.googleapis.com/css2?family=Montserrat:wght@300;400;500;600;700;800&display=swap">
<style>
:root{
  --blue:#0392cd;
  --dark:#333333;
  --hero:#444444;
  --footer:#1e1e1e;
  --navy:#0d4a5a;
  --ink:#2b2b2b;
  --muted:#6a6a6a;
  --light:#efefef;
  --white:#ffffff;
}
*{margin:0;padding:0;box-sizing:border-box}
html,body{width:675px;height:1200px;overflow:hidden;background:var(--white)}
body{font-family:"Montserrat",sans-serif;color:var(--ink)}
.page{position:relative;width:675px;height:1200px;overflow:hidden}
.abs{position:absolute}

.topbar{left:0;top:0;width:675px;height:21px;background:var(--dark)}
.topbar .dot{position:absolute;top:6px;width:8px;height:8px;border-radius:50%;background:#fff}
.topbar svg{position:absolute;top:5px}

.brand{left:0;top:38px;width:675px;text-align:center;font-size:16px;font-weight:700;letter-spacing:.2px;color:var(--ink)}
.nav{left:0;top:71px;width:675px;display:flex;justify-content:center;gap:24px;font-size:8px;font-weight:600;color:var(--navy)}
.header-rule{left:0;top:101px;width:675px;height:1px;background:#ddd}

.hero{left:0;top:101px;width:675px;height:190px;background:var(--hero)}
.hero h1{position:absolute;left:90px;top:42px;font-size:22px;font-weight:300;color:#fff;letter-spacing:.3px}
.hero p{position:absolute;left:90px;top:78px;width:232px;font-size:9.5px;line-height:15px;color:#fff}
.hero .ghost{position:absolute;left:90px;top:134px;width:60px;height:17px;border:1.5px solid #fff;color:#fff;font-size:5.5px;font-weight:800;text-align:center;line-height:14px}
.hero .portrait{position:absolute;left:398px;top:4px;width:187px;height:186px;border-radius:90px 90px 0 0;background:linear-gradient(180deg,#5a4a44 0%,#b8927e 45%,#f1cfe0 100%)}
.arrow{position:absolute;top:80px;width:41px;height:29px;background:#fff}
.arrow svg{position:absolute;left:15px;top:8px}

.avatar{left:91px;top:312px;width:120px;height:120px;border-radius:50%;border:3px solid var(--blue);background:#fff}
.avatar .photo{position:absolute;left:5px;top:5px;width:104px;height:104px;border-radius:50%;background:linear-gradient(160deg,#d9d9d9,#8a8a8a 70%,#3a3a3a)}
.branch{left:205px;top:328px}
.about-title{left:314px;top:309px;font-size:12.5px;font-weight:700;letter-spacing:.5px}
.about-text{left:314px;top:334px;width:272px;font-size:9.5px;line-height:15.2px;color:var(--muted)}
.btn-blue{left:314px;top:407px;width:87px;height:26px;background:var(--blue);color:#fff;font-size:6.5px;font-weight:700;text-align:center;line-height:26px}

.recent{left:0;top:455px;width:675px;height:263px;background:var(--light)}
.section-title{left:0;width:675px;text-align:center;font-size:12.5px;font-weight:700;letter-spacing:.6px;color:var(--ink)}
.card{position:absolute;top:50px;width:148px;height:192px;background:#fff;box-shadow:0 1px 3px rgba(0,0,0,.15)}
.card .thumb{height:88px}
.card .date{position:absolute;left:14px;top:100px;font-size:6px;font-weight:600;color:var(--blue)}
.card h3{position:absolute;left:14px;top:119px;width:125px;font-size:9.5px;font-weight:500;line-height:15px;letter-spacing:.3px;color:var(--ink)}
.card .more{position:absolute;left:14px;top:161px;width:54px;height:16px;background:var(--dark);color:#fff;font-size:4.5px;font-weight:800;text-align:center;line-height:16px}

.tile{position:absolute;top:770px;width:169px;height:168px}
.product{position:absolute;left:16px;top:16px;width:137px;height:136px;background:#fff}
.product .tag{position:absolute;left:16px;top:42px;font-size:6px;color:var(--blue);font-weight:500}
.product h4{position:absolute;left:16px;top:62px;width:115px;font-size:9.5px;line-height:15px;font-weight:700;letter-spacing:.4px}
.product .price{position:absolute;left:16px;top:110px;font-size:9.5px;font-weight:700;color:#666}

.footer{left:0;top:938px;width:675px;height:262px;background:var(--footer);color:#fff}
.footer .ttl{position:absolute;left:0;top:18px;width:675px;text-align:center;font-size:13px;font-weight:700;letter-spacing:.4px}
.footer .name{position:absolute;left:90px;top:59px;font-size:13px;font-weight:700}
.footer .rule{position:absolute;left:90px;top:92px;width:95px;height:2px;background:#fff}
.footer .info{position:absolute;left:91px;font-size:8px;font-weight:700}
.footer .soc{position:absolute;top:190px;width:9px;height:9px;border-radius:50%;background:#fff}
.footer .copy{position:absolute;left:90px;top:235px;font-size:8px;font-weight:700;color:#666}
.field{position:absolute;border:1px solid #777;border-radius:3px;font-size:8px;color:#ccc;padding:0 10px;line-height:26px}
.field.active{border-color:#fff;color:#999}
.send{position:absolute;left:344px;top:172px;width:240px;height:27px;background:var(--blue);border-radius:3px;text-align:center;line-height:27px;font-size:8px;color:#fff}
</style>
</head>
<body>
<div class="page">

  <div class="abs topbar">
    <span class="dot" style="left:90px"></span>
    <span class="dot" style="left:105px"></span>
    <span class="dot" style="left:120px"></span>
    <svg style="left:552px" width="10" height="10" viewBox="0 0 10 10"><circle cx="4" cy="4" r="3" fill="none" stroke="#fff" stroke-width="1.2"/><line x1="6.2" y1="6.2" x2="9" y2="9" stroke="#fff" stroke-width="1.3"/></svg>
    <svg style="left:571px" width="13" height="10" viewBox="0 0 13 10"><path d="M0 1h13M0 5h13M0 9h13" stroke="#fff" stroke-width="1.2"/></svg>
  </div>

  <div class="abs brand">KAREL DUMONTE</div>
  <nav class="abs nav"><span>HOME</span><span>ABOUT ME</span><span>BLOG</span><span>SERVICES</span><span>CONTACT ME</span></nav>
  <div class="abs header-rule"></div>

  <section class="abs hero">
    <h1>E-COMMERCE EXPERT</h1>
    <p>Inspiring &amp; Helping Entrepreneurs around the world achieve success....</p>
    <div class="ghost">LEARN MORE</div>
    <div class="portrait" role="img" aria-label="Portrait of Karel Dumonte smiling, wearing glasses and a pink shirt"></div>
    <div class="arrow" style="left:0"><svg width="10" height="14" viewBox="0 0 10 14"><path d="M8 1L2 7l6 6" fill="none" stroke="#333" stroke-width="1.3"/></svg></div>
    <div class="arrow" style="left:634px"><svg width="10" height="14" viewBox="0 0 10 14"><path d="M2 1l6 6-6 6" fill="none" stroke="#333" stroke-width="1.3"/></svg></div>
  </section>

  <div class="abs avatar"><div class="photo" role="img" aria-label="Portrait photo of Karel Dumonte, hand on chin"></div></div>
  <svg class="abs branch" width="50" height="96" viewBox="0 0 50 96">
    <path d="M3 20 Q10 9 32 9 M6 44 H40 M3 68 Q10 80 32 80" fill="none" stroke="var(--blue)" stroke-width="2"/>
    <circle cx="32" cy="9" r="8" fill="var(--blue)"/>
    <circle cx="40" cy="44" r="8" fill="var(--blue)"/>
    <circle cx="32" cy="80" r="8" fill="var(--blue)"/>
  </svg>
  <h2 class="abs about-title">ABOUT ME</h2>
  <p class="abs about-text">Lorem ipsum dolor sit amet, consectetur adipisicing elit, sed do eiusmod tempor incididunt ut labore et dolore magna aliqua. Ut enim ad minim.</p>
  <div class="abs btn-blue">LEARN MORE</div>

  <section class="abs recent">
    <h2 class="abs section-title" style="top:18px">RECENT POST</h2>
    <article class="card" style="left:91px">
      <div class="thumb" role="img" aria-label="Man sitting at a meeting table in an office" style="background:linear-gradient(135deg,#c9d2d6,#5f7487 60%,#2f3b48)"></div>
      <div class="date">December, 2017</div>
      <h3>Best Way to Overcome Frustration in Sales</h3>
      <div class="more">SEE MORE</div>
    </article>
    <article class="card" style="left:264px">
      <div class="thumb" role="img" aria-label="Young man with phone at a street cafe" style="background:linear-gradient(135deg,#d8cfc0,#8a7a6a 55%,#3d3530)"></div>
      <div class="date">December, 2017</div>
      <h3>How to Increase Your Income While Moving..</h3>
      <div class="more">SEE MORE</div>
    </article>
    <article class="card" style="left:436px">
      <div class="thumb" role="img" aria-label="Video still of a man by the sea" style="position:relative;background:linear-gradient(180deg,#8fb5c9,#2f5e78 55%,#1d2a36)">
        <svg style="position:absolute;left:58px;top:28px" width="34" height="34" viewBox="0 0 34 34"><circle cx="17" cy="17" r="15" fill="rgba(0,0,0,.35)" stroke="#fff" stroke-width="2.5"/><path d="M13 10l11 7-11 7z" fill="#fff"/></svg>
      </div>
      <div class="date">December, 2017</div>
      <h3>How I've made Over 6 Figures in Door-To...</h3>
      <div class="more">SEE MORE</div>
    </article>
  </section>

  <h2 class="abs section-title" style="top:737px">SERVICES AND PRODUCTS</h2>

  <div class="tile" style="left:0;background:linear-gradient(180deg,#3b5368,#2a3a49)" role="img" aria-label="Course promotion background">
    <div class="product">
      <div class="tag">Course</div>
      <h4>Spark-2-Scale Launch Course</h4>
      <div class="price">$1,497</div>
    </div>
  </div>
  <div class="tile" style="left:169px;background:linear-gradient(180deg,#2a2a2a,#555 60%,#1b1b1b)" role="img" aria-label="Book cover for Relentless Path by Karel Dumonte"></div>
  <div class="tile" style="left:338px;background:linear-gradient(180deg,#4ab2e6,#2e9fd8)" role="img" aria-label="Illustration of hands holding a phone surrounded by shopping icons"></div>
  <div class="tile" style="left:507px;width:168px;background:linear-gradient(180deg,#2a2a2a,#555 60%,#1b1b1b)" role="img" aria-label="Book cover for Relentless Path by Karel Dumonte"></div>

  <footer class="abs footer">
    <div class="ttl">GET IN TOUCH WITH ME</div>
    <div class="name">KAREL DUMONTE</div>
    <div class="rule"></div>
    <div class="info" style="top:123px">HELLO@DUMONTESTUDIO.EXAMPLE</div>
    <div class="info" style="top:153px">+01 55 555 0199</div>
    <span class="soc" style="left:91px"></span>
    <span class="soc" style="left:109px"></span>
    <span class="soc" style="left:128px"></span>
    <div class="copy">COPYRIGHT © 2017 KAREL DUMONTE</div>

    <div class="field active" style="left:344px;top:62px;width:109px;height:27px">Enter your name</div>
    <div class="field" style="left:474px;top:62px;width:110px;height:27px">Enter your adresse</div>
    <div class="field" style="left:344px;top:104px;width:240px;height:52px;line-height:28px">Enter your message</div>
    <div class="send">Send Message</div>
  </footer>
</div>
</body>
</html>
```